New Facebook Banner

Hi
We are operating Ramen shop in Australia.(http://mizorinoodlebar.example)
I want to create new design for our Facebook banner and title is "Free Ramen on your Birthday".
Sample attached is our existing banner design. We would like to make it more modern and sophisticated.
We are so looking forward to seeing your design for our free ramen promotion.

https://www.facebook.com/mizorinoodlebar/

Industry/Entity Type

Japanese Restaurant

Font styles to use
Sans Serif

```html
<!DOCTYPE html>
<html lang="en">
<head>
<meta charset="utf-8">
<title>Mizori Noodle Bar – Page</title>
<link href="https://fonts.googleapis.com/css2?family=Arimo:wght@400;700&family=Lato:wght@400;700&family=Lilita+One&display=swap" rel="stylesheet">
<style>
:root{
  --bar:#3b5998;
  --bar-dark:#2d4373;
  --page:#e9ebee;
  --white:#ffffff;
  --line:#dddfe2;
  --text:#1d2129;
  --muted:#4b4f56;
  --soft:#90949c;
  --blue:#4080ff;
  --link:#365899;
  --brand-red:#c8102e;
  --brand-navy:#1f2e7a;
  --green:#42b72a;
}
*{box-sizing:border-box;margin:0;padding:0}
html,body{width:1200px;height:683px;overflow:hidden}
body{position:relative;background:var(--page);font-family:"Lato",Arial,sans-serif;color:var(--text)}
.abs{position:absolute}

/* top bar */
.topbar{left:0;top:0;width:1200px;height:43px;background:var(--bar);border-bottom:1px solid var(--bar-dark)}
.topbar__mark{left:83px;top:10px;width:24px;height:24px;background:var(--white);border-radius:2px}
.search{left:114px;top:10px;width:446px;height:24px;background:var(--white);border-radius:2px;font-family:"Arimo",Arial,sans-serif;font-size:13px;padding:4px 6px;color:var(--text)}
.search__btn{right:0;top:0;width:46px;height:24px;background:#f6f7f9;border-left:1px solid var(--line);display:flex;align-items:center;justify-content:center}
.topbar__user{left:746px;top:14px;color:var(--white);font-family:"Arimo",Arial,sans-serif;font-size:12px}
.topbar__sep{top:11px;width:1px;height:20px;background:var(--bar-dark)}
.topbar__home{left:853px;top:14px;color:var(--white);font-family:"Arimo",Arial,sans-serif;font-size:12px;font-weight:700}
.topbar__home span{display:inline-block;background:var(--bar-dark);font-size:10px;padding:1px 3px;margin-left:4px}
.topbar__icons{left:933px;top:10px}

/* left column */
.avatar{left:82px;top:55px;width:172px;height:172px;background:var(--white);border:1px solid var(--line);display:flex;align-items:center;justify-content:center;gap:8px}
.avatar__dot{width:18px;height:18px;border-radius:50%;background:var(--brand-red)}
.avatar__name{font-family:"Lato",Arial,sans-serif;font-weight:700;font-size:30px;color:var(--brand-navy)}
.page-name{left:82px;top:240px;font-family:"Lato",Arial,sans-serif;font-weight:400;font-size:23px;line-height:26px;color:var(--text)}
.verified{display:inline-block;width:20px;height:20px;border-radius:50%;background:#8d949e;vertical-align:-3px;margin-left:8px;position:relative}
.handle{left:82px;top:296px;font-size:13px;color:var(--soft)}
.nav{left:82px;top:331px;width:172px;list-style:none}
.nav li{height:32px;line-height:32px;padding-left:11px;font-size:14px;color:var(--muted)}
.nav .is-active{background:#dfe1e6;border-left:3px solid var(--bar);padding-left:8px;font-weight:700;color:var(--text)}
.create{left:90px;top:635px;width:97px;height:24px;background:var(--green);border:1px solid #36a420;border-radius:2px;color:var(--white);font-family:"Arimo",Arial,sans-serif;font-size:12px;text-align:center;line-height:22px}

/* cover */
.cover{left:266px;top:43px;width:828px;height:316px;overflow:hidden;
  background:radial-gradient(ellipse at 45% 85%,#d9792a 0%,#9a3f26 35%,#5a2a2c 70%,#3d2528 100%)}
.cover__title{left:0;top:70px;width:828px;text-align:center;font-family:"Lilita One",Impact,sans-serif;font-size:68px;line-height:76px;color:var(--white);letter-spacing:1px;
  text-shadow:0 0 4px #000,0 0 8px #000,0 0 14px rgba(0,0,0,.8)}
.cover__sub{left:0;top:241px;width:828px;text-align:center;font-family:"Arimo",Arial,sans-serif;font-weight:700;font-size:21px;color:var(--white);text-shadow:0 0 4px #000,0 0 6px #000}

/* action bar */
.actions{left:266px;top:359px;width:828px;height:54px;background:var(--white);border:1px solid var(--line);border-top:none}
.btn-group{left:13px;top:13px;display:flex;height:28px;border:1px solid #ccd0d5;border-radius:2px;background:#f6f7f9;font-family:"Arimo",Arial,sans-serif}
.btn{display:flex;align-items:center;gap:5px;padding:0 9px;font-size:12px;font-weight:700;color:var(--muted);border-right:1px solid #ccd0d5}
.btn:last-child{border-right:none}
.contact{left:529px;top:13px;width:286px;height:28px;background:var(--blue);border-radius:2px;color:var(--white);font-family:"Arimo",Arial,sans-serif;font-size:14px;font-weight:700;text-align:center;line-height:28px}

/* composer */
.composer{left:266px;top:426px;width:502px;height:181px;background:var(--white);border:1px solid var(--line);border-radius:3px;overflow:hidden}
.composer__tabs{height:34px;background:#f6f7f9;border-bottom:1px solid var(--line);display:flex;align-items:center;padding-left:13px;gap:10px;font-family:"Arimo",Arial,sans-serif;font-size:12px;font-weight:700}
.tab{display:flex;align-items:center;gap:6px}
.tab--link{color:var(--link)}
.composer__sel{right:26px;top:10px;width:16px;height:14px;background:#d8dbe0}
.composer__body{left:11px;top:54px;display:flex;gap:11px}
.post-avatar{width:40px;height:26px;display:flex;align-items:center;gap:3px}
.post-avatar__dot{width:8px;height:8px;border-radius:50%;background:var(--brand-red)}
.post-avatar__name{font-size:9px;font-weight:700;color:var(--brand-navy)}
.composer__text{font-family:"Lato",Arial,sans-serif;font-size:12.5px;line-height:17px;color:var(--soft);white-space:nowrap}

/* info card */
.info{left:781px;top:427px;width:313px;height:67px;background:var(--white);border:1px solid var(--line);border-radius:3px;padding:12px 12px}
.info__line{font-family:"Lato",Arial,sans-serif;font-size:13.5px;color:var(--text)}
.rating{margin-top:6px;display:flex;align-items:center;gap:4px;font-size:16px;color:#4267b2}
</style>
</head>
<body>

<header class="topbar abs">
  <div class="topbar__mark abs"></div>
  <div class="search abs">mizorinoodlebar.example
    <div class="search__btn abs">
      <svg width="14" height="14" viewBox="0 0 14 14"><circle cx="6" cy="6" r="4.5" fill="none" stroke="#4b4f56" stroke-width="1.6"/><line x1="9.2" y1="9.2" x2="13" y2="13" stroke="#4b4f56" stroke-width="1.8"/></svg>
    </div>
  </div>
  <div class="topbar__user abs">dana whitfield</div>
  <div class="topbar__sep abs" style="left:839px"></div>
  <div class="topbar__home abs">Home<span>5</span></div>
  <div class="topbar__sep abs" style="left:917px"></div>
  <svg class="topbar__icons abs" width="165" height="22" viewBox="0 0 165 22" fill="#1d2b4c">
    <circle cx="8" cy="7" r="4"/><path d="M1 20c0-5 3-8 7-8s7 3 7 8z"/><circle cx="15" cy="6" r="3.5"/>
    <path d="M36 3h14v9h-8l-4 3v-3h-2z"/><path d="M44 8h12v9h-2v3l-4-3h-6z"/>
    <circle cx="80" cy="11" r="9"/><circle cx="80" cy="11" r="6" fill="#3b5998"/>
    <rect x="101" y="2" width="1" height="18" fill="#2d4373"/>
    <rect x="113" y="9" width="10" height="9"/><path d="M115 9V6a3 3 0 0 1 6 0v3" fill="none" stroke="#1d2b4c" stroke-width="2"/>
    <rect x="126" y="8" width="7" height="2"/><rect x="126" y="12" width="7" height="2"/><rect x="126" y="16" width="7" height="2"/>
    <path d="M144 8h10l-5 6z"/>
  </svg>
</header>

<aside>
  <div class="avatar abs"><span class="avatar__dot"></span><span class="avatar__name">Mizori</span></div>
  <h1 class="page-name abs">Mizori Noodle<br>Bar<span class="verified"><svg class="abs" style="left:4px;top:5px" width="12" height="10" viewBox="0 0 12 10"><path d="M1 5l3.5 3.5L11 1.5" fill="none" stroke="#fff" stroke-width="2"/></svg></span></h1>
  <div class="handle abs">@mizorinoodlebar</div>
  <ul class="nav abs">
    <li class="is-active">Home</li><li>About</li><li>Notes</li><li>Email Signup</li><li>Photos</li><li>Reviews</li><li>Videos</li><li>Likes</li><li>Posts</li>
  </ul>
  <div class="create abs">Create a Page</div>
</aside>

<section class="cover abs" role="img" aria-label="Close-up photo of a birthday cake with lit striped candles, blurred warm orange and red tones">
  <div class="cover__title abs">FREE RAMEN ON<br>YOUR BIRTHDAY</div>
  <div class="cover__sub abs">Find out more on mizorinoodlebar.example</div>
</section>

<div class="actions abs">
  <div class="btn-group abs">
    <div class="btn"><svg width="13" height="12" viewBox="0 0 13 12"><path d="M0 5h3v7H0zM4 5l3-5c1.5 0 2 1 1.6 2.4L8 5h4c1 0 1 1 .8 1.6L11 11.5c-.3.4-.6.5-1 .5H4z" fill="#4267b2"/></svg>Liked<svg width="8" height="5" viewBox="0 0 8 5"><path d="M0 0h8L4 5z" fill="#4b4f56"/></svg></div>
    <div class="btn"><svg width="14" height="13" viewBox="0 0 14 13"><path d="M1 1h12v8H6l-3 3V9H1z" fill="#90949c"/></svg>Message</div>
    <div class="btn"><svg width="14" height="3" viewBox="0 0 14 3" fill="#90949c"><circle cx="1.5" cy="1.5" r="1.5"/><circle cx="7" cy="1.5" r="1.5"/><circle cx="12.5" cy="1.5" r="1.5"/></svg>More<svg width="8" height="5" viewBox="0 0 8 5"><path d="M0 0h8L4 5z" fill="#4b4f56"/></svg></div>
  </div>
  <div class="contact abs">Contact Us</div>
</div>

<section class="composer abs">
  <div class="composer__tabs">
    <div class="tab"><svg width="16" height="16" viewBox="0 0 16 16"><rect width="16" height="16" rx="2" fill="#4267b2"/><path d="M4 12l1-3 5-5 2 2-5 5z" fill="#fff"/></svg>Status</div>
    <div class="tab tab--link"><svg width="16" height="16" viewBox="0 0 16 16"><rect x="1" y="1" width="14" height="14" rx="2" fill="none" stroke="#f5793a" stroke-width="2"/><path d="M4 12l3-4 2 2 2-3 2 5z" fill="#f5793a"/></svg>Photo/Video</div>
  </div>
  <div class="composer__sel abs"></div>
  <div class="composer__body abs">
    <div class="post-avatar"><span class="post-avatar__dot"></span><span class="post-avatar__name">Mizori</span></div>
    <p class="composer__text">We specialize in ramen with "Tonkotsu soup", broth of pork bone.<br>Ramen is one of the representative dishes in Japan following<br>Tempura and Sushi. among the variety of flavour for soup Ramen is one of the<br>representative dishes in Japan following Tempura and Sushi. among the<br>&nbsp;variety of flavour for soup Ramen is one of the representative dishes in<br>Japan following Tempura and Sushi. among the variety of flavour for soup</p>
  </div>
</section>

<section class="info abs">
  <div class="info__line">Business service • London, United Kingdom</div>
  <div class="rating">4.7
    <svg width="80" height="14" viewBox="0 0 80 14" fill="#4267b2">
      <path id="star" d="M7 0l2 4.6 5 .4-3.8 3.3 1.2 5L7 10.6 2.6 13.3l1.2-5L0 5l5-.4z"/>
      <use href="#star" x="16"/><use href="#star" x="32"/><use href="#star" x="48"/>
      <path d="M71 0l2 4.6 5 .4-3.8 3.3 1.2 5L71 10.6z" fill="#c4cde0"/>
      <path d="M71 0l-2 4.6-5 .4 3.8 3.3-1.2 5L71 10.6z"/>
    </svg>
  </div>
</section>

</body>
</html>
```